Large walking and cycling programme needs a vision poster

We need a visually inspiring poster that promotes the Kestrel Wheelway Schemes' vision, key priorities and values. The Kestrel Wheelway Scheme is a large project in Auckland that will deliver more walking and cycling infrastructure to the city. <br/>Elements that need to be included in the poster are:<br/>Vision - Choice connections for our communities<br/>Key priorities - Our story, Smarter procurement, Our resources<br/>Values - Courageous, Communication, Just do it, Own the bigger programme, Openness and collaboration, Flexibility and open to change

```html
<!DOCTYPE html>
<html lang="en">
<head>
<meta charset="utf-8">
<title>Kestrel Wheelway Scheme – Vision, Key Priorities and Values</title>
<link href="https://fonts.googleapis.com/css2?family=Poppins:wght@200;300;400;700;800&display=swap" rel="stylesheet">
<style>
  :root {
    --orange: #e07d12;
    --ink: #000000;
    --paper: #ffffff;
    --backdrop: #e6e6e6;
  }
  * { margin: 0; padding: 0; box-sizing: border-box; }
  html, body {
    width: 1180px;
    height: 1200px;
    overflow: hidden;
    background: var(--backdrop);
    font-family: "Poppins", sans-serif;
  }
  .poster {
    position: absolute;
    left: 228px;
    top: 38px;
    width: 724px;
    height: 1123px;
    background: var(--ink);
    color: var(--paper);
    overflow: hidden;
  }
  .poster > * { position: absolute; }
  .decor { left: 0; top: 0; width: 724px; height: 1123px; }

  .title-small {
    left: 72px;
    font-weight: 300;
    font-size: 36px;
    letter-spacing: 2px;
    line-height: 1;
  }
  .title-the { top: 70px; }
  .title-scheme { top: 160px; }
  .title-name {
    left: 72px;
    top: 108px;
    font-weight: 800;
    font-size: 47px;
    line-height: 1;
    color: var(--orange);
    letter-spacing: -0.5px;
    white-space: nowrap;
  }

  .column-letter {
    width: 80px;
    text-align: center;
    line-height: 1;
  }
  .vision-letter {
    left: 290px;
    font-weight: 800;
    font-size: 76px;
    color: var(--orange);
  }
  .values-letter {
    left: 450px;
    font-weight: 300;
    font-size: 66px;
    color: var(--paper);
  }

  .heading-key {
    left: 70px;
    top: 586px;
    font-weight: 300;
    font-size: 70px;
    line-height: 1;
    letter-spacing: 8px;
  }
  .heading-priorities {
    font-weight: 800;
    font-size: 70px;
    line-height: 1;
    letter-spacing: 7px;
    top: 650px;
    white-space: nowrap;
  }
  .heading-prior { left: 70px; }
  .heading-tie { left: 350px; }

  .tag-list { list-style: none; }
  .tag-list li {
    position: absolute;
    left: 0;
    white-space: nowrap;
  }
  .tag {
    display: inline-block;
    background: var(--paper);
    color: var(--ink);
    font-weight: 400;
    font-size: 16.5px;
    line-height: 19px;
    letter-spacing: -0.6px;
    padding: 0 12px 0 2px;
  }
  .vision-list { left: 526px; top: 392px; }
  .priorities-list { left: 70px; top: 826px; }
  .values-list { left: 376px; top: 749px; }

  .web-bar {
    left: 72px;
    top: 1040px;
    width: 582px;
    height: 27px;
    background: var(--orange);
    color: var(--ink);
    text-align: center;
    font-weight: 400;
    font-size: 19px;
    line-height: 27px;
    letter-spacing: 8px;
  }
</style>
</head>
<body>
  <main class="poster">
    <svg class="decor" viewBox="0 0 724 1123" aria-hidden="true">
      <g stroke-linecap="round" fill="none">
        <line x1="70" y1="408" x2="657" y2="168" stroke="var(--orange)" stroke-width="5"/>
        <line x1="70" y1="393" x2="252" y2="320" stroke="var(--paper)" stroke-width="5"/>
        <line x1="474" y1="255" x2="657" y2="183" stroke="var(--paper)" stroke-width="5"/>
      </g>
      <g fill="none" stroke="var(--orange)" stroke-width="4" stroke-linejoin="miter">
        <polyline points="532,340 541,350 532,360"/>
        <polyline points="544,340 553,350 544,360"/>
        <polyline points="556,340 565,350 556,360"/>
        <polyline points="311,902 320,912 311,922"/>
        <polyline points="323,902 332,912 323,922"/>
        <polyline points="335,902 344,912 335,922"/>
        <polyline points="72,754 82,763 92,754"/>
        <polyline points="72,765 82,774 92,765"/>
        <polyline points="72,776 82,785 92,776"/>
      </g>
    </svg>

    <p class="title-small title-the">THE</p>
    <h1 class="title-name">KESTREL WHEELWAY</h1>
    <p class="title-small title-scheme">SCHEME</p>

    <span class="column-letter values-letter" style="top:322px">V</span>
    <span class="column-letter values-letter" style="top:388px">A</span>
    <span class="column-letter values-letter" style="top:454px">L</span>
    <span class="column-letter values-letter" style="top:521px">U</span>
    <span class="column-letter values-letter" style="top:588px">E</span>
    <span class="column-letter values-letter" style="top:654px">S</span>

    <span class="column-letter vision-letter" style="top:406px">V</span>
    <span class="column-letter vision-letter" style="top:486px">I</span>
    <span class="column-letter vision-letter" style="top:570px">S</span>
    <span class="column-letter vision-letter" style="top:650px">I</span>
    <span class="column-letter vision-letter" style="top:731px">O</span>
    <span class="column-letter vision-letter" style="top:815px">N</span>

    <h2 class="heading-key">KEY</h2>
    <span class="heading-priorities heading-prior">PRIOR</span>
    <span class="heading-priorities heading-tie">TIE</span>

    <ul class="tag-list vision-list">
      <li style="top:0"><span class="tag">Choice</span></li>
      <li style="top:24px"><span class="tag">Connections</span></li>
      <li style="top:49px"><span class="tag">For Our</span></li>
      <li style="top:73px"><span class="tag">Communities</span></li>
    </ul>

    <ul class="tag-list priorities-list">
      <li style="top:0"><span class="tag">Our Story</span></li>
      <li style="top:38px"><span class="tag">Smarter Procurement</span></li>
      <li style="top:76px"><span class="tag">Our Resources</span></li>
    </ul>

    <ul class="tag-list values-list">
      <li style="top:0"><span class="tag">Courageous</span></li>
      <li style="top:38px"><span class="tag">Communication</span></li>
      <li style="top:76px"><span class="tag">Just Do It</span></li>
      <li style="top:114px"><span class="tag">Own The Bigger Programme</span></li>
      <li style="top:152px"><span class="tag">Openness And Collaboration</span></li>
      <li style="top:190px"><span class="tag">Flexibility And Open To Change</span></li>
    </ul>

    <p class="web-bar">WWW.KESTRELWAY.NZ</p>
  </main>
</body>
</html>
```